Brookside Grocer

Hope all is well!

Wanted to make business cards for my father. His name is Faisal Qureshi and owns convenience stores. I have attached logo :)

He does not want any title just simple name and phone. An email would be nice as well.

Faisal Qureshi
Cell: 413-585-2046
Store: 413-719-4820

Brooksidegrocer512@fernpost.com

The design and style is totally up to you :) The colors we were looking for were the same as logo :)

```html
<!DOCTYPE html>
<html lang="en">
<head>
<meta charset="utf-8">
<title>Brookside Grocer — Business Card</title>
<link href="https://fonts.googleapis.com/css2?family=Lato:wght@400;700;900&display=swap" rel="stylesheet">
<style>
  :root {
    --backdrop: #3a3a3a;
    --brand-red: #e9333a;
    --brand-navy: #243a7a;
    --paper: #ffffff;
    --ink: #3d3d3d;
  }
  html, body {
    margin: 0;
    padding: 0;
    width: 1200px;
    height: 689px;
    overflow: hidden;
    background: var(--backdrop);
    font-family: "Lato", sans-serif;
  }
  .canvas {
    position: relative;
    width: 1200px;
    height: 689px;
  }
  .card {
    position: absolute;
    top: 200px;
    width: 500px;
    height: 286px;
    overflow: hidden;
  }
  .card-front {
    left: 70px;
    background: var(--brand-red);
    display: flex;
    align-items: center;
    justify-content: center;
  }
  .front-brand {
    color: var(--paper);
    font-weight: 900;
    font-size: 42px;
    letter-spacing: 1px;
    text-transform: uppercase;
  }
  .card-back {
    left: 630px;
    background: var(--paper);
  }
  .corner-block {
    position: absolute;
    right: 0;
    top: 34px;
    width: 48px;
    height: 48px;
    background: var(--brand-red);
  }
  .back-brand {
    position: absolute;
    right: 64px;
    top: 78px;
    color: var(--brand-navy);
    font-weight: 900;
    font-size: 26px;
    text-transform: uppercase;
    letter-spacing: 0.5px;
  }
  .name-band {
    position: absolute;
    left: 0;
    top: 128px;
    width: 258px;
    height: 44px;
    background: var(--brand-navy);
    display: flex;
    align-items: center;
    padding-left: 24px;
    box-sizing: border-box;
  }
  .person-name {
    color: var(--paper);
    font-weight: 700;
    font-size: 19px;
    text-transform: uppercase;
    letter-spacing: 0.5px;
  }
  .contact-list {
    position: absolute;
    left: 54px;
    bottom: 30px;
    margin: 0;
    padding: 0;
    list-style: none;
    color: var(--ink);
    font-size: 13px;
    line-height: 20px;
  }
  .contact-list li {
    display: flex;
    align-items: center;
    gap: 8px;
  }
  .contact-icon {
    width: 11px;
    height: 11px;
    fill: var(--brand-navy);
    flex: none;
  }
</style>
</head>
<body>
<main class="canvas">
  <section class="card card-front">
    <span class="front-brand">Brookside Grocer</span>
  </section>

  <section class="card card-back">
    <div class="corner-block"></div>
    <span class="back-brand">Brookside Grocer</span>
    <div class="name-band"><span class="person-name">Faisal Qureshi</span></div>
    <ul class="contact-list">
      <li>
        <svg class="contact-icon" viewBox="0 0 24 24" aria-hidden="true"><path d="M6.6 10.8a15 15 0 0 0 6.6 6.6l2.2-2.2c.3-.3.7-.4 1-.2 1.1.4 2.3.6 3.6.6.6 0 1 .4 1 1V20c0 .6-.4 1-1 1A17 17 0 0 1 3 4c0-.6.4-1 1-1h3.5c.6 0 1 .4 1 1 0 1.3.2 2.5.6 3.6.1.3 0 .7-.2 1z"/></svg>
        413-719-4820
      </li>
      <li>
        <svg class="contact-icon" viewBox="0 0 24 24" aria-hidden="true"><path d="M7 1h10a2 2 0 0 1 2 2v18a2 2 0 0 1-2 2H7a2 2 0 0 1-2-2V3a2 2 0 0 1 2-2zm0 3v14h10V4zm5 15.5a1 1 0 1 0 0 2 1 1 0 0 0 0-2z"/></svg>
        413-585-2046
      </li>
      <li>
        <svg class="contact-icon" viewBox="0 0 24 24" aria-hidden="true"><path d="M2 5h20v14H2zm2 2v.5l8 5 8-5V7zm0 2.8V17h16V9.8l-8 5z"/></svg>
        Brooksidegrocer512@fernpost.com
      </li>
    </ul>
  </section>
</main>
</body>
</html>
```